Powerpoint template for corporate presentations

Our company, ClinicMeadowlane, has recently undertaken a re-branding overhaul for our website and corporate materials (color scheme, letterhead, biz cards). In support of this re-branding effort, we need a powerpoint template for corporate presentations that will reflect the look and feel of the website.

We would like to receive a powerpoint template that contains the following slide layouts:
- title slide
- section header slide
- content slide (title & content)
- closing/acknowledgement slide

The website design, colors, fonts and images are included as attachments for your reference.An example powerpoint template is included, if needed for your reference. We would like to see the icons and colors used to make the presentation more visually appealing.

Specific comments regarding the example ppt with content attached to this brief:
- the content slides seem a bit sparse and do not have much space for text/charts.
- For the content slides, a white/light background and dark text is still expected.
- For the section header and closing slides, we would like to see a layout more engaging than just the blue background. Note: a blue or colored background is acceptable for these slides so long as the text color has enough contrast to be visible.

Industry/Entity Type

It Company

```html
<!DOCTYPE html>
<html lang="en">
<head>
<meta charset="utf-8">
<title>ClinicMeadowlane – Presentation Template</title>
<link rel="stylesheet" href="https://fonts.googleapis.com/css2?family=Open+Sans:ital,wght@0,400;0,600;0,700;1,700&display=swap">
<style>
  :root {
    --board: #c89d6e;
    --slide-light: #f7f7f7;
    --slide-dark: #4d4d4d;
    --slide-darker: #3f3f3f;
    --accent-yellow: #f6dc6c;
    --accent-blue: #1aa9d8;
    --accent-light-blue: #8fd4f0;
    --ink: #222222;
    --ink-soft: #555555;
    --bar-dark: #474a4f;
    --photo-light: #dcdcdc;
    --photo-dark: #5a5a5a;
  }
  * { margin: 0; padding: 0; box-sizing: border-box; }
  html, body { width: 1200px; height: 907px; overflow: hidden; }
  body {
    background: var(--board);
    font-family: "Open Sans", Arial, sans-serif;
    position: relative;
  }
  .slide {
    position: absolute;
    width: 377px;
    height: 282px;
    overflow: hidden;
  }
  .slide--light { background: linear-gradient(180deg, #fdfdfd 0%, var(--slide-light) 60%, #ececec 100%); }
  .slide--dark { background: linear-gradient(180deg, var(--slide-dark) 0%, var(--slide-darker) 100%); }

  .slide--title { left: 36px; top: 24px; }
  .slide--section { left: 788px; top: 24px; }
  .slide--chart { left: 413px; top: 311px; }
  .slide--points { left: 36px; top: 592px; }
  .slide--closing { left: 788px; top: 596px; }

  .scene-photo { position: absolute; left: 0; right: 0; }
  .scene-photo--light {
    top: 110px; bottom: 0;
    background: linear-gradient(180deg, rgba(220,220,220,0) 0%, var(--photo-light) 45%, #cfcfcf 100%);
  }
  .scene-photo--faint {
    top: 120px; bottom: 0;
    background: linear-gradient(180deg, rgba(230,230,230,0) 0%, rgba(225,225,225,.7) 100%);
  }
  .scene-photo--dark {
    top: 110px; bottom: 0;
    background: linear-gradient(180deg, rgba(90,90,90,0) 0%, var(--photo-dark) 55%, #474747 100%);
  }

  .brand {
    position: absolute;
    font-weight: 400;
    color: var(--ink-soft);
    white-space: nowrap;
  }
  .brand--hero { top: 48px; left: 0; right: 0; text-align: center; font-size: 24px; letter-spacing: .2px; }
  .brand--footer { right: 10px; bottom: 9px; font-size: 8.5px; }

  .title-band {
    position: absolute; left: 0; right: 0; top: 179px; height: 60px;
    background: rgba(160,160,160,.35);
    text-align: center; padding-top: 10px;
  }
  .title-band__title { font-size: 20px; font-weight: 400; color: var(--accent-yellow); line-height: 1.1; }
  .title-band__subtitle { font-size: 12.5px; color: var(--accent-yellow); line-height: 1.3; }

  .section-title {
    position: absolute; left: 0; right: 0; text-align: center;
    font-size: 18px; font-weight: 700; color: var(--accent-yellow);
  }
  .slide--section .section-title { top: 45px; }
  .slide--closing .section-title { top: 43px; }

  .thank-you {
    position: absolute; left: 0; right: 0; top: 130px;
    text-align: center; font-size: 26px; color: var(--accent-yellow);
    transform: rotate(3deg);
  }

  .content-title {
    position: absolute; left: 0; right: 0; top: 27px; text-align: center;
    font-size: 14px; font-weight: 700; font-style: italic; color: var(--ink);
  }
  .accent-rule {
    position: absolute; top: 50px; left: 109px; width: 150px; height: 3px; display: flex;
  }
  .accent-rule span { flex: 1; }
  .accent-rule .y { background: var(--accent-yellow); }
  .accent-rule .b { background: var(--accent-blue); }
  .accent-rule .d { background: var(--bar-dark); }
  .accent-rule .l { background: var(--accent-light-blue); }

  .page-badge { position: absolute; right: 9px; top: 10px; width: 18px; height: 19px; }

  .chart { position: absolute; left: 0; top: 0; width: 377px; height: 282px; }
  .chart text { font-family: "Open Sans", Arial, sans-serif; font-size: 7.5px; fill: #444; }

  .icon-circle {
    position: absolute; left: 37px; top: 68px; width: 128px; height: 128px;
    border: 1.5px solid #333; border-radius: 50%; background: #ffffff;
  }
  .icon-circle__art {
    position: absolute; left: 30px; top: 20px; width: 66px; height: 86px;
    background: linear-gradient(180deg, #eaf6fb 0%, #8fd0ea 100%);
    border-radius: 8px;
  }
  .point-list { position: absolute; left: 170px; top: 94px; list-style: none; }
  .point-list li {
    font-size: 8.5px; color: var(--ink-soft); line-height: 13.4px;
    display: flex; align-items: center; gap: 7px;
  }
  .point-list svg { width: 7px; height: 7px; }
</style>
</head>
<body>

  <section class="slide slide--light slide--title">
    <div class="scene-photo scene-photo--light" role="img" aria-label="Soft grey photo of frosted glass cubes on a reflective surface"></div>
    <div class="brand brand--hero">ClinicMeadowlane™</div>
    <div class="title-band">
      <h1 class="title-band__title">Presentation title Here</h1>
      <p class="title-band__subtitle">Presentation sub title here</p>
    </div>
  </section>

  <section class="slide slide--dark slide--section">
    <div class="scene-photo scene-photo--dark" role="img" aria-label="Dark toned photo of glass cubes fading into shadow"></div>
    <h2 class="section-title">Your Section Title comes Here</h2>
  </section>

  <section class="slide slide--light slide--chart">
    <div class="scene-photo scene-photo--faint" role="img" aria-label="Faint backdrop photo of glass cubes"></div>
    <h2 class="content-title">Your Content Slide comes here</h2>
    <div class="accent-rule"><span class="y"></span><span class="b"></span><span class="d"></span><span class="l"></span></div>
    <svg class="page-badge" viewBox="0 0 18 19"><polygon points="9,0 18,19 0,19" fill="#333"/><text x="9" y="16.5" font-size="7" fill="#fff" text-anchor="middle" font-family="Open Sans, sans-serif">1</text></svg>
    <svg class="chart" viewBox="0 0 377 282" role="img" aria-label="Clustered bar chart of three series across four categories">
      <g stroke="#c8c8c8" stroke-width="0.6">
        <line x1="81" y1="201" x2="262" y2="201"/>
        <line x1="81" y1="65" x2="81" y2="201"/>
      </g>
      <g text-anchor="end">
        <text x="75" y="203.5">0</text><text x="75" y="180.8">1</text><text x="75" y="158.1">2</text>
        <text x="75" y="135.5">3</text><text x="75" y="112.8">4</text><text x="75" y="90.1">5</text><text x="75" y="67.5">6</text>
      </g>
      <g fill="var(--bar-dark)">
        <rect x="87" y="103.4" width="9" height="97.6"/><rect x="132" y="144.3" width="9" height="56.7"/>
        <rect x="177" y="121.6" width="9" height="79.4"/><rect x="222" y="98.9" width="9" height="102.1"/>
      </g>
      <g fill="var(--accent-blue)">
        <rect x="97" y="146.5" width="9" height="54.5"/><rect x="142" y="101.1" width="9" height="99.9"/>
        <rect x="187" y="160.1" width="9" height="40.9"/><rect x="232" y="137.4" width="9" height="63.6"/>
      </g>
      <g fill="var(--accent-yellow)">
        <rect x="107" y="155.6" width="9" height="45.4"/><rect x="152" y="155.6" width="9" height="45.4"/>
        <rect x="197" y="132.9" width="9" height="68.1"/><rect x="242" y="87.5" width="9" height="113.5"/>
      </g>
      <g text-anchor="middle">
        <text x="103" y="214">Category 1</text><text x="148" y="214">Category 2</text>
        <text x="193" y="214">Category 3</text><text x="238" y="214">Category 4</text>
      </g>
      <rect x="271" y="126" width="4" height="4" fill="var(--bar-dark)"/><text x="279" y="130.5">Series 1</text>
      <rect x="271" y="138" width="4" height="4" fill="var(--accent-blue)"/><text x="279" y="142.5">Series 2</text>
      <rect x="271" y="150" width="4" height="4" fill="var(--accent-yellow)"/><text x="279" y="154.5">Series 3</text>
    </svg>
    <div class="brand brand--footer">ClinicMeadowlane™</div>
  </section>

  <section class="slide slide--light slide--points">
    <div class="scene-photo scene-photo--faint" role="img" aria-label="Faint backdrop photo of glass cubes"></div>
    <h2 class="content-title">Your Content Slide comes here</h2>
    <div class="accent-rule"><span class="y"></span><span class="b"></span><span class="d"></span><span class="l"></span></div>
    <svg class="page-badge" viewBox="0 0 18 19"><polygon points="9,0 18,19 0,19" fill="#333"/><text x="9" y="16.5" font-size="7" fill="#fff" text-anchor="middle" font-family="Open Sans, sans-serif">1</text></svg>
    <div class="icon-circle">
      <div class="icon-circle__art" role="img" aria-label="Illustration of a laboratory flask with bubbles"></div>
    </div>
    <ul class="point-list">
      <li><svg viewBox="0 0 8 8"><polyline points="1,4 3,6.5 7,1.5" fill="none" stroke="#555" stroke-width="1.2"/></svg>Your Points come here</li>
      <li><svg viewBox="0 0 8 8"><polyline points="1,4 3,6.5 7,1.5" fill="none" stroke="#555" stroke-width="1.2"/></svg>Your Points come here</li>
      <li><svg viewBox="0 0 8 8"><polyline points="1,4 3,6.5 7,1.5" fill="none" stroke="#555" stroke-width="1.2"/></svg>Your Points come here</li>
      <li><svg viewBox="0 0 8 8"><polyline points="1,4 3,6.5 7,1.5" fill="none" stroke="#555" stroke-width="1.2"/></svg>Your Points come here</li>
      <li><svg viewBox="0 0 8 8"><polyline points="1,4 3,6.5 7,1.5" fill="none" stroke="#555" stroke-width="1.2"/></svg>Your Points come here</li>
      <li><svg viewBox="0 0 8 8"><polyline points="1,4 3,6.5 7,1.5" fill="none" stroke="#555" stroke-width="1.2"/></svg>Your Points come here</li>
    </ul>
    <div class="brand brand--footer">ClinicMeadowlane™</div>
  </section>

  <section class="slide slide--dark slide--closing">
    <div class="scene-photo scene-photo--dark" role="img" aria-label="Dark toned photo of glass cubes fading into shadow"></div>
    <h2 class="section-title">Closing slide comes here</h2>
    <p class="thank-you">Thank you</p>
  </section>

</body>
</html>
```